Create Template Proposal Coversheet

We need a proposal Cover Sheet & Page Template for residential architectural projects. For the Cover Sheet, we want a variety of images blends and set as a background image for the title of the proposal for prospective clients. We need it in a format that we can type over the top of the image (maybe whited-out in the middle) so we can use it for all our proposals. Our logo should be clear and sharp in a corner (but we will leave that up to the designer. Not all images need to be used. For the Page Template we want a consistent look on the page with our logo, company address & contact information and a design element that ties the entire proposal together. Our proposals consist of a Cover page, Project information sheet, a picture of the property, the proposal for services (3-5 pages), Expect fees page and a timeline page.

Target Market(s)

Homeowners, 35 - 60 years old

Industry/Entity Type

Architecture

Font styles to use
Serif

Colors
3176b5
f68d4c
ec1f27
fbee3f

Requirements
Must have
• The cover should have a nice blend of images - looking for something that shows the whole design process - from initial sketches to working drawings, construction and finished home. These images are background to the title of the proposal

```html
<!DOCTYPE html>
<html lang="en">
<head>
<meta charset="utf-8">
<title>Proposal Cover Sheet</title>
<link rel="stylesheet" href="https://fonts.googleapis.com/css2?family=Roboto+Slab:wght@400;700&display=swap">
<style>
  :root {
    --sheet-white: #ffffff;
    --accent-orange: #f7931e;
    --blue-light: #3ab0e0;
    --blue-mid: #3a6fc4;
    --blue-deep: #2f3590;
    --grey-light: #f0f0f0;
    --grey-mid: #cfcfcf;
    --brand-navy: #2c3a8e;
    --brand-orange: #f68d4c;
  }
  * { margin: 0; padding: 0; box-sizing: border-box; }
  html, body {
    width: 856px;
    height: 1200px;
    overflow: hidden;
    background: var(--sheet-white);
  }
  .cover {
    position: relative;
    width: 856px;
    height: 1200px;
    overflow: hidden;
    background: var(--sheet-white);
    font-family: "Roboto Slab", Georgia, serif;
  }
  .cover-art {
    position: absolute;
    inset: 0;
    width: 856px;
    height: 1200px;
  }
  .proposal-heading {
    position: absolute;
    left: 293px;
    top: 624px;
    color: var(--sheet-white);
  }
  .proposal-title {
    font-weight: 700;
    font-size: 44px;
    line-height: 1.1;
    letter-spacing: 0.3px;
  }
  .proposal-subtitle {
    margin-top: 6px;
    font-weight: 400;
    font-size: 26px;
    line-height: 1.2;
  }
  .brand {
    position: absolute;
    left: 40px;
    top: 1110px;
    display: flex;
    align-items: center;
    gap: 12px;
  }
  .brand-mark {
    width: 22px;
    height: 22px;
    background: var(--brand-orange);
  }
  .brand-name {
    font-weight: 700;
    font-size: 24px;
    letter-spacing: 0.5px;
    color: var(--brand-navy);
  }
</style>
</head>
<body>
<main class="cover">
  <svg class="cover-art" viewBox="0 0 856 1200" xmlns="http://www.w3.org/2000/svg">
    <defs>
      <linearGradient id="constructionTone" x1="0" y1="0" x2="1" y2="1">
        <stop offset="0" stop-color="var(--grey-light)"/>
        <stop offset="1" stop-color="var(--grey-mid)"/>
      </linearGradient>
      <linearGradient id="blueprintTone" x1="1" y1="0" x2="0" y2="1">
        <stop offset="0" stop-color="var(--blue-light)"/>
        <stop offset="0.45" stop-color="var(--blue-mid)"/>
        <stop offset="1" stop-color="var(--blue-deep)"/>
      </linearGradient>
    </defs>

    <rect class="construction-photo" x="0" y="0" width="856" height="1200"
          fill="url(#constructionTone)" role="img"
          aria-label="Greyscale photograph of a timber-framed entrance porch under construction"/>

    <path class="blueprint-panel" d="M0 828 Q 305 372 856 124 L856 1200 L0 1200 Z"
          fill="url(#blueprintTone)" role="img"
          aria-label="Rolled architectural blueprints tinted blue"/>

    <path class="accent-curve-top" d="M0 822 Q 303 366 856 118"
          fill="none" stroke="var(--accent-orange)" stroke-width="9"/>

    <path class="footer-panel" d="M0 1002 Q 420 975 856 1195 L856 1200 L0 1200 Z"
          fill="var(--sheet-white)"/>

    <path class="accent-curve-bottom" d="M0 1002 Q 420 975 856 1195"
          fill="none" stroke="var(--accent-orange)" stroke-width="5"/>
  </svg>

  <header class="proposal-heading">
    <h1 class="proposal-title">Proposal Title here</h1>
    <p class="proposal-subtitle">Sub text here</p>
  </header>

  <div class="brand">
    <span class="brand-mark"></span>
    <span class="brand-name">HARLAN J REEVE ARCHITECT</span>
  </div>
</main>
</body>
</html>
```